New Business Card Design Project

double sided business cards. i would like to design a business card with the logo attached . that logo being centered on 1 side and then my info on the other.

Boyd Whitfield CEO
Phone# 334-571-2806
Boyd@brightoakupkeep.com

Contact Information for Business Card

double sided one side the Logo attached below that saying Home Maintenance and Repair Specialists then on back my info Boyd Whitfield CEO Home Maintenance Specialist Phone# 334-571-2806 Boyd@brightoakupkeep.com

Font styles to use
Serif

Colors
0054AA
0677BA
7BADD7
CADEEF
E8F1F8
FFC000
F8CF3A
FAE287
FDF2CF
FEFAEE

Requirements
Must have
• double sided logo attached on one side with colors blue and gold. black background info on the other side

```html
<!DOCTYPE html>
<html lang="en">
<head>
<meta charset="utf-8">
<title>Brightoak Upkeep – Business Card</title>
<link href="https://fonts.googleapis.com/css2?family=Poppins:wght@400;500;600;700&display=swap" rel="stylesheet">
<style>
  :root {
    --page: #ffffff;
    --card-core: #15252b;
    --card-edge: #01070b;
    --gold: #ffc000;
    --gold-soft: #f8cf3a;
    --blue: #0677ba;
    --white: #ffffff;
  }
  * { box-sizing: border-box; margin: 0; padding: 0; }
  html, body {
    width: 1200px; height: 1200px; overflow: hidden;
    background: var(--page);
    font-family: "Poppins", sans-serif;
  }
  .sheet {
    width: 1200px; height: 1200px;
    display: flex; flex-direction: column;
    align-items: center; justify-content: center; gap: 60px;
  }
  .card {
    position: relative;
    width: 840px; height: 480px;
    background: radial-gradient(ellipse at 55% 45%, var(--card-core) 0%, #06141a 45%, var(--card-edge) 100%);
    overflow: hidden;
    box-shadow: 0 18px 40px rgba(0,0,0,.28);
  }
  .accent-block {
    position: absolute; width: 150px; height: 70px; background: var(--gold);
  }
  .accent-block--left { left: 0; bottom: 60px; }
  .accent-block--right { right: 0; top: 60px; }

  .brand {
    display: flex; align-items: center; gap: 16px;
    color: var(--blue); font-weight: 700; letter-spacing: 2px;
    white-space: nowrap;
  }
  .brand__mark { background: var(--gold); flex: none; }

  .card--front .brand {
    position: absolute; left: 50%; top: 150px; transform: translateX(-50%);
    font-size: 54px;
  }
  .card--front .brand__mark { width: 34px; height: 34px; }
  .tagline {
    position: absolute; left: 178px; bottom: 128px;
    color: var(--white); white-space: nowrap;
    font-weight: 600; font-size: 29px; letter-spacing: 5px;
  }

  .card--back .brand {
    position: absolute; right: 46px; top: 70px; font-size: 28px; gap: 10px;
  }
  .card--back .brand__mark { width: 18px; height: 18px; }
  .contact {
    position: absolute; left: 92px; bottom: 58px; color: var(--white);
  }
  .contact__name { font-size: 46px; font-weight: 500; line-height: 1.1; white-space: nowrap; }
  .contact__name strong { font-weight: 700; }
  .contact__role { font-size: 22px; font-weight: 400; }
  .contact__title { color: var(--gold); font-size: 22px; font-weight: 500; margin-bottom: 22px; }
  .contact__list { list-style: none; }
  .contact__item {
    display: flex; align-items: center; gap: 20px;
    font-size: 21px; line-height: 1.75; font-weight: 400;
  }
  .contact__icon { width: 24px; height: 24px; flex: none; }
</style>
</head>
<body>
<main class="sheet">

  <section class="card card--front" aria-label="Card front">
    <div class="accent-block accent-block--right"></div>
    <div class="accent-block accent-block--left"></div>
    <div class="brand"><span class="brand__mark"></span>BRIGHTOAK UPKEEP</div>
    <p class="tagline">HOME MAINTENANCE SPECIALIST</p>
  </section>

  <section class="card card--back" aria-label="Card back">
    <div class="brand"><span class="brand__mark"></span>BRIGHTOAK UPKEEP</div>
    <div class="contact">
      <h1 class="contact__name"><strong>Boyd</strong> Whitfield <span class="contact__role">- CEO</span></h1>
      <p class="contact__title">Home Maintenance Specialist</p>
      <ul class="contact__list">
        <li class="contact__item">
          <svg class="contact__icon" viewBox="0 0 24 24"><path fill="#ffc000" d="M6.6 10.8a15.1 15.1 0 0 0 6.6 6.6l2.2-2.2a1 1 0 0 1 1-.25 11.4 11.4 0 0 0 3.6.57 1 1 0 0 1 1 1V20a1 1 0 0 1-1 1A17 17 0 0 1 3 4a1 1 0 0 1 1-1h3.5a1 1 0 0 1 1 1c0 1.25.2 2.45.57 3.57a1 1 0 0 1-.25 1z"/></svg>
          334-571-2806
        </li>
        <li class="contact__item">
          <svg class="contact__icon" viewBox="0 0 24 24"><rect x="2" y="5" width="20" height="14" rx="2" fill="#ffc000"/><path d="M3 6l9 7 9-7" fill="none" stroke="#06141a" stroke-width="1.6"/></svg>
          Boyd@brightoakupkeep.com
        </li>
        <li class="contact__item">
          <svg class="contact__icon" viewBox="0 0 24 24" fill="none" stroke="#ffc000" stroke-width="2"><circle cx="12" cy="12" r="9.5"/><ellipse cx="12" cy="12" rx="4" ry="9.5"/><path d="M2.5 12h19M4 7h16M4 17h16"/></svg>
          www.brightoakupkeep.com
        </li>
      </ul>
    </div>
  </section>

</main>
</body>
</html>
```